Stationery Design Project

We need, stationary designs for a store of children and juvenile furniture.
we have the logo. also need tags for the furniture with enought space to include description and options , maybe a 4" x 6" tag.

Target Market(s)

Parents of childrens and teens

Industry/Entity Type

Store

```html
<!DOCTYPE html>
<html lang="en">
<head>
<meta charset="utf-8">
<title>LittleNest Letterhead</title>
<link rel="stylesheet" href="https://fonts.googleapis.com/css2?family=Cinzel:wght@600&family=Noto+Sans:wght@700&display=swap">
<style>
  :root {
    --backdrop: #e4e4e4;
    --paper: #fafafa;
    --sky-top: #b8e2e7;
    --sky-mid: #cdeaee;
    --sky-fade: #fafafa;
    --accent-teal: #5bc4cf;
    --accent-orange: #f07f2e;
    --band-tan: #edc595;
    --name-white: #ffffff;
  }
  html, body {
    margin: 0;
    padding: 0;
    width: 1200px;
    height: 1000px;
    overflow: hidden;
    background: var(--backdrop);
  }
  .letterhead {
    position: absolute;
    left: 248px;
    top: 43px;
    width: 705px;
    height: 913px;
    background: var(--paper);
    overflow: hidden;
  }
  .sky-artwork {
    position: absolute;
    left: 0;
    top: 0;
    width: 100%;
    height: 360px;
    background: linear-gradient(to bottom, var(--sky-top) 0%, var(--sky-mid) 50%, var(--sky-fade) 100%);
  }
  .contact-line {
    position: absolute;
    left: 77px;
    top: 831px;
    margin: 0;
    font-family: "Noto Sans", sans-serif;
    font-weight: 700;
    font-size: 11px;
    line-height: 14px;
    letter-spacing: 0.3px;
    color: var(--accent-teal);
    white-space: nowrap;
  }
  .footer-rule {
    position: absolute;
    left: 0;
    top: 847px;
    width: 100%;
    height: 4px;
    background: var(--accent-orange);
  }
  .footer-band {
    position: absolute;
    left: 0;
    top: 851px;
    width: 100%;
    height: 62px;
    background: var(--band-tan);
  }
  .brand-mark {
    position: absolute;
    left: 552px;
    top: 786px;
    width: 72px;
    height: 72px;
    background: var(--accent-teal);
  }
  .brand-name {
    position: absolute;
    right: 20px;
    top: 861px;
    margin: 0;
    font-family: "Cinzel", serif;
    font-weight: 600;
    font-size: 27px;
    line-height: 34px;
    letter-spacing: 0.5px;
    color: var(--name-white);
    white-space: nowrap;
  }
</style>
</head>
<body>
  <main class="letterhead">
    <div class="sky-artwork" role="img" aria-label="Soft illustrated blue sky with white clouds fading into the page"></div>
    <p class="contact-line">phone: 4410-25836 adress: Maple Avenue -218 e-mail: hello@littlenest.com</p>
    <div class="footer-rule"></div>
    <div class="footer-band"></div>
    <div class="brand-mark" role="img" aria-label="LittleNest brand mark"></div>
    <p class="brand-name">LittleNest</p>
  </main>
</body>
</html>
```